BrightHarbor logo and website profile

BrightHarbor is a newly started business angel network investing in entrepreneurs and start-ups. We need a smart looking logo and website design (based on Wordpress).
The aim of the site is to attract 2 customer segments;
1) Entrepreneurs and start-ups looking for investors
2) Investors/ business angels looking to become part of a larger network of investors for better access to investments
A successful conversion on the website would be for the entrepreneur or investor sending us an e-mail to submit their investment proposal, inquire about our services or ask to join the network of investors.
The website should focus on presenting Bright Harbor and our offerings towards the 2 customer segments. This is NOT a platform like e.g. finchly.co.
Sites we like;
http://demo.pelmora.net/themes/orchid/agency/
http://www.tarnwickadvisory.no (it's a bit bleak - needs a little more color)
Target Market(s)
Two target markets; 1) entrepreneurs looking for investors 2) business angels looking for investment opportunities
Industry/Entity Type
Investment
Requirements
Must have
- The keywords we want associated with our brand are;
Innovation – Integrity – Knowledgeable – Growth – Entrepreneurship
Logodesign (symbol and smart presentation of the company name - bright harbor, both with and without .com)
Wordpress design, pages we need:
- landing page with clear CTA for entrepreneurs and clear CTA for investors
- Portfolio overview of investments made
- General page for our approach, services etc
- Contact us page
- Favicon
- News
- Header/footer information
Other functionality we need;
- Social media integration
The design must support mobile and iPads as well.
We like: less is more :)

```html
<!DOCTYPE html>
<html lang="en">
<head>
<meta charset="utf-8">
<title>Bright Harbor</title>
<link rel="stylesheet" href="https://fonts.googleapis.com/css2?family=Oswald:wght@500&family=Yanone+Kaffeesatz:wght@500&family=Cuprum:ital@1&family=PT+Sans&display=swap">
<style>
:root{
  --outer:#777777;
  --header:#dedede;
  --rule:#333333;
  --panel:#ebebeb;
  --ink:#444444;
  --muted:#8a8a8a;
  --body:#555555;
  --accent:#d0021b;
  --footer:#000000;
  --copy-band:#cccccc;
  --dark:#2e2e2e;
}
*{margin:0;padding:0;box-sizing:border-box}
html,body{width:1200px;height:955px;overflow:hidden;background:var(--outer)}
.page{position:absolute;left:110px;top:0;width:980px;height:953px;background:var(--panel);border-left:1px solid #555;border-bottom:2px solid #222}
.site-header{position:absolute;left:0;top:0;width:980px;height:48px;background:var(--header);border-bottom:4px solid var(--rule)}
.brand{position:absolute;left:12px;top:8px;display:flex;align-items:center;gap:8px;font-family:"Oswald",sans-serif;font-weight:500;font-size:24px;line-height:28px;color:var(--rule);letter-spacing:.5px}
.brand-mark{width:20px;height:20px;background:var(--accent)}
.main-nav{position:absolute;left:384px;top:13px;display:flex;font-family:"Cuprum",sans-serif;font-style:italic;font-size:16px;color:#333}
.main-nav a{color:inherit;text-decoration:none;margin-right:41px}
.hero{position:absolute;left:0;top:48px;width:980px;height:447px}
.segment{position:absolute;top:527px}
.segment h2{font-family:"Oswald",sans-serif;font-weight:500;font-size:26px;line-height:28px;color:var(--ink);letter-spacing:-.3px;transform:scaleX(.88);transform-origin:left}
.segment .tagline{font-family:"Yanone Kaffeesatz",sans-serif;font-weight:500;font-size:16px;color:var(--muted);text-align:right;margin-top:-3px}
.segment p{font-family:Arial,Helvetica,sans-serif;font-size:12.4px;line-height:14px;color:var(--body);margin-top:22px}
.cta{display:flex;align-items:center;gap:10px;margin-top:24px;font-family:Arial,Helvetica,sans-serif;font-size:11px;line-height:13px;color:var(--accent)}
.investors{left:21px;width:350px}
.entrepreneurs{left:530px;width:364px}
.social{position:absolute;left:744px;top:800px;width:232px;height:48px;background:#d4d4d4;border-radius:4px 4px 0 0;display:flex;gap:11px;padding:8px 9px}
.social span{width:34px;height:34px;border-radius:6px;background:linear-gradient(#9a9a9a,#5e5e5e)}
.site-footer{position:absolute;left:0;top:848px;width:980px;height:40px;background:var(--footer);display:flex;justify-content:center;align-items:center;font-family:Arial,Helvetica,sans-serif;font-size:12.5px;color:#fff}
.site-footer .dot{margin:0 11px;color:#aaa}
.copyright{position:absolute;left:0;top:888px;width:980px;height:63px;background:var(--copy-band);text-align:center;padding-top:14px;font-family:"PT Sans",sans-serif;font-size:12px;color:#111}
</style>
</head>
<body>
<div class="page">
  <header class="site-header">
    <div class="brand"><span class="brand-mark"></span>BRIGHT HARBOR</div>
    <nav class="main-nav">
      <a>HOME</a><a>PORTFOLIO</a><a>APPROACH AND SERVICES</a><a>NEWS</a><a>CONTACT US</a>
    </nav>
  </header>

  <svg class="hero" viewBox="0 0 980 447" xmlns="http://www.w3.org/2000/svg">
    <defs>
      <linearGradient id="leftPhoto" x1="0" y1="0" x2="1" y2="0">
        <stop offset="0" stop-color="#f7f5f2"/><stop offset=".6" stop-color="#e9dfd2"/><stop offset="1" stop-color="#c9b8a0"/>
      </linearGradient>
      <linearGradient id="rightPhoto" x1="0" y1="0" x2="1" y2="0">
        <stop offset="0" stop-color="#3a3a3a"/><stop offset=".35" stop-color="#d8d4d0"/><stop offset="1" stop-color="#fafafa"/>
      </linearGradient>
    </defs>
    <rect width="980" height="447" fill="var(--dark)"/>
    <rect y="416" width="980" height="10" fill="#cfcfcf"/>
    <path d="M0 0H496V330C492 395 440 425 310 426H0Z" fill="#cfcfcf"/>
    <path d="M506 0H980V426H676C560 425 510 395 506 330Z" fill="#cfcfcf"/>
    <path d="M0 0H496V330C490 385 440 416 310 417H0Z" fill="url(#leftPhoto)" role="img" aria-label="Photo of a smiling businessman in a beige suit with arms crossed"/>
    <path d="M506 0H980V417H676C565 416 512 385 506 330Z" fill="url(#rightPhoto)" role="img" aria-label="Photo of a young businessman in a dark vest and white shirt with arms crossed"/>
  </svg>

  <section class="segment investors">
    <h2>INVESTORS / BUSINESS ANGELS</h2>
    <div class="tagline">looking for better access to investments</div>
    <p>Are you wondering where to invest your money and looking for a successfull ROI? You just came to the right place, we can help you decide and find a good business investment the you desire.</p>
    <div class="cta">
      <svg width="27" height="36" viewBox="0 0 27 36"><path d="M2 12L13.5 3 25 12V30H2Z" fill="#e34a5a"/><path d="M2 12L13.5 22 25 12" fill="none" stroke="#fff" stroke-width="1.5"/><circle cx="13.5" cy="13" r="3" fill="none" stroke="#fff" stroke-width="1.2"/></svg>
      <span>contact us and get a business proposal or<br>submit invsestment proposal</span>
    </div>
  </section>

  <section class="segment entrepreneurs">
    <h2>ENTREPRENEURS AND STARTUPS</h2>
    <div class="tagline">looking for investors</div>
    <p>Have a business in mind but don't have enought funds to continue with the venture? This is the right place to take your business into a higher next and look for investors to help you achive the business of your dreams.</p>
    <div class="cta">
      <svg width="27" height="36" viewBox="0 0 27 36"><path d="M2 12L13.5 3 25 12V30H2Z" fill="#e34a5a"/><path d="M2 12L13.5 22 25 12" fill="none" stroke="#fff" stroke-width="1.5"/><circle cx="13.5" cy="13" r="3" fill="none" stroke="#fff" stroke-width="1.2"/></svg>
      <span>contact us and submit your business proposal</span>
    </div>
  </section>

  <div class="social" aria-label="Social media links"><span></span><span></span><span></span><span></span><span></span></div>

  <footer class="site-footer">
    <span>HOME</span><span class="dot">·</span><span>PORTFOLIO</span><span class="dot">·</span><span>APPROACH AND SERVICES</span><span class="dot">·</span><span>NEWS</span><span class="dot">·</span><span>CONTACT US</span>
  </footer>
  <div class="copyright">© Copyright 2013 BRIGHT HARBOR All Rights Reserved.</div>
</div>
</body>
</html>
```